Need an ebook cover for a memoir about growing up in NYC in the 90s and getting in lots of trouble.

Harbor Lane Rebel is the true story of an over-privileged hoodlum
growing up in Manhattan in the 90s during the golden era of hip-hop. The book follows the troubled youth all the way from hanging off the back of subway cars at fourteen, through a romance with a mafia princess doomed for disaster, to a law school class where the unreformed miscreant sits politely with his hand raised. The cover should feature a white teenager, perhaps in a puffy Ridgeline Coat jacket, in NYC -- or whatever you feel; I am open. I've attached a sample of the memoir for your reference. I've also attached a sample of what I think the title should look like: Harbor Lane Rebel; Marlow Quint; A Memoir.

The name of the author is Marlow Quint. It is not Tobin Fairley.

```html
<!DOCTYPE html>
<html lang="en">
<head>
<meta charset="utf-8">
<title>Harbor Lane Rebel — A Memoir</title>
<link rel="stylesheet" href="https://fonts.googleapis.com/css2?family=Cinzel+Decorative:wght@400&family=Cinzel:wght@400&display=swap">
<style>
  :root {
    --sky: #ffffff;
    --fog: #e9ebed;
    --mist: #b4b8bc;
    --trees: #3d4044;
    --trees-deep: #24262a;
    --road: #46484b;
    --snow: #e4e6e8;
    --ink: #4a4f58;
    --author: #ffffff;
  }
  html, body {
    margin: 0;
    padding: 0;
    width: 848px;
    height: 1200px;
    overflow: hidden;
    background: var(--sky);
  }
  .cover {
    position: relative;
    width: 848px;
    height: 1200px;
    overflow: hidden;
    background: var(--sky);
  }
  .cover-photo {
    position: absolute;
    inset: 0;
    background:
      /* dark road in the foreground, narrowing toward the fog */
      radial-gradient(ellipse 520px 300px at 424px 1230px, var(--road) 0%, rgba(70,72,75,0.85) 55%, rgba(70,72,75,0) 100%),
      /* tall tree mass along the right edge */
      radial-gradient(ellipse 360px 620px at 860px 820px, var(--trees-deep) 0%, rgba(36,38,42,0.85) 45%, rgba(61,64,68,0.35) 75%, rgba(61,64,68,0) 100%),
      /* lower tree line on the left */
      radial-gradient(ellipse 380px 300px at -20px 930px, var(--trees-deep) 0%, rgba(36,38,42,0.8) 50%, rgba(61,64,68,0) 100%),
      /* misty gap in the middle distance */
      radial-gradient(ellipse 260px 220px at 430px 760px, var(--fog) 0%, rgba(233,235,237,0) 100%),
      linear-gradient(180deg,
        var(--sky) 0%,
        var(--sky) 42%,
        var(--fog) 58%,
        var(--mist) 72%,
        var(--trees) 88%,
        var(--trees-deep) 100%);
  }
  .title-block {
    position: absolute;
    top: 176px;
    left: 0;
    right: 0;
    margin: 0;
    text-align: center;
    color: var(--ink);
  }
  .book-title {
    margin: 0;
    font-family: "Cinzel Decorative", "Cinzel", serif;
    font-weight: 400;
    font-size: 76px;
    line-height: 64px;
    letter-spacing: 0;
  }
  .book-subtitle {
    position: absolute;
    top: 384px;
    left: 0;
    right: 0;
    margin: 0;
    text-align: center;
    font-family: "Cinzel Decorative", "Cinzel", serif;
    font-weight: 400;
    font-size: 43px;
    letter-spacing: 1px;
    color: var(--ink);
  }
  .author-name {
    position: absolute;
    top: 1000px;
    left: 0;
    right: 0;
    margin: 0;
    text-align: center;
    font-family: "Cinzel", serif;
    font-weight: 400;
    font-size: 47px;
    letter-spacing: 1px;
    color: var(--author);
  }
</style>
</head>
<body>
  <main class="cover">
    <div class="cover-photo" role="img" aria-label="Photograph of a lone young man seen from behind, walking away down a misty road between tall bare winter trees, with snow along the roadsides"></div>
    <h1 class="title-block book-title">HARBOR LANE<br>REBEL</h1>
    <p class="book-subtitle">A Memoir</p>
    <p class="author-name">MARLOW QUINT</p>
  </main>
</body>
</html>
```